Business Card Design Project

We are an incubator company that helps young entrepreneur to launch new ideas into the market. We will be targeting investors or likewise; Angels, young entrepreneurs and technopreneurs.

Our logo is being tasked by artflockly to design, therefore there is no logo for now.
You can us Lanternfold Pte Ltd as the logo for the time being.

Please let us have some versions of modern and yet professional designs; for words, you can indicate e.g (address), (Title)

thanks

Target Market(s)

young entrepreneurs
angels, investors

Industry/Entity Type

Business

Colors
3176b5
ffffff

Requirements
Must have
• able to project out our name; Lanternfold
Should not have
• Nothing childish or cartoon

```html
<!DOCTYPE html>
<html lang="en">
<head>
<meta charset="utf-8">
<title>Lanternfold Business Card</title>
<link href="https://fonts.googleapis.com/css2?family=Questrial&display=swap" rel="stylesheet">
<style>
  :root {
    --backdrop: #d8d7d5;
    --brand-blue: #3176b5;
    --brand-deep: #1d5aa6;
    --brand-ink: #1e5ba8;
    --brand-light: #7fc3ef;
    --white: #ffffff;
    --card-shadow: rgba(0, 0, 0, 0.22);
  }
  html, body {
    margin: 0;
    padding: 0;
    overflow: hidden;
  }
  body {
    width: 1200px;
    height: 900px;
    background: var(--backdrop);
    font-family: "Questrial", sans-serif;
    position: relative;
  }
  .card {
    position: absolute;
    top: 300px;
    width: 525px;
    height: 300px;
    border-radius: 22px;
    box-shadow: 0 14px 30px var(--card-shadow);
    overflow: hidden;
  }
  .card--front {
    left: 50px;
    background: var(--white);
  }
  .card--back {
    left: 625px;
    background: linear-gradient(100deg, var(--brand-deep) 0%, var(--brand-blue) 60%, #2f7cc4 100%);
  }

  /* Front */
  .brand {
    position: absolute;
    left: 34px;
    top: 88px;
    color: var(--brand-ink);
  }
  .brand__mark {
    width: 54px;
    height: 54px;
    background: var(--brand-ink);
    margin-bottom: 18px;
    margin-left: 2px;
  }
  .brand__name {
    font-size: 42px;
    letter-spacing: 1px;
    line-height: 1;
    text-transform: uppercase;
  }
  .brand__tagline {
    font-size: 11px;
    letter-spacing: 2.6px;
    text-transform: uppercase;
    margin-top: 6px;
    padding-left: 28px;
  }
  .splash {
    position: absolute;
    right: 0;
    top: 0;
    width: 260px;
    height: 300px;
  }

  /* Back */
  .contact {
    position: absolute;
    top: 122px;
    left: 0;
    width: 100%;
    display: flex;
    color: var(--white);
  }
  .contact__person {
    width: 230px;
    text-align: right;
    padding-right: 16px;
    padding-top: 4px;
  }
  .contact__name {
    font-size: 19px;
    font-weight: 700;
  }
  .contact__title {
    font-size: 13px;
    margin-top: 2px;
  }
  .contact__divider {
    width: 1px;
    height: 84px;
    background: rgba(255, 255, 255, 0.85);
  }
  .contact__list {
    list-style: none;
    margin: 0;
    padding: 0 0 0 14px;
    font-size: 15px;
    line-height: 19px;
  }
  .contact__item {
    display: flex;
    align-items: center;
    gap: 6px;
  }
  .contact__icon {
    width: 16px;
    height: 16px;
    flex: none;
  }
</style>
</head>
<body>

  <section class="card card--front" aria-label="Card front">
    <div class="brand">
      <div class="brand__mark"></div>
      <div class="brand__name">Lanternfold</div>
      <div class="brand__tagline">Launching New Ideas Ahead</div>
    </div>
    <svg class="splash" viewBox="0 0 260 300" role="img" aria-label="Blue watercolour splash sweeping diagonally across the card">
      <defs>
        <linearGradient id="splashTone" x1="0" y1="1" x2="1" y2="0">
          <stop offset="0" stop-color="#1f5fb0"/>
          <stop offset="0.5" stop-color="#5fb2e8"/>
          <stop offset="1" stop-color="#2a6fc0"/>
        </linearGradient>
      </defs>
      <path d="M150 0 L230 0 C215 60 190 90 170 150 C150 210 120 260 95 300 L20 300 C50 250 80 210 100 160 C120 100 130 50 150 0 Z" fill="url(#splashTone)"/>
    </svg>
  </section>

  <section class="card card--back" aria-label="Card back">
    <div class="contact">
      <div class="contact__person">
        <div class="contact__name">Dana Whitlow</div>
        <div class="contact__title">Manager</div>
      </div>
      <div class="contact__divider"></div>
      <ul class="contact__list">
        <li class="contact__item">
          <svg class="contact__icon" viewBox="0 0 16 16"><path d="M4 1 L6.5 4.5 L5 6.5 C6 8.5 7.5 10 9.5 11 L11.5 9.5 L15 12 L13 15 C7 14.5 1.5 9 1 3 Z" fill="#fff"/></svg>
          555 014 2283
        </li>
        <li class="contact__item">
          <svg class="contact__icon" viewBox="0 0 16 16" fill="none" stroke="#fff" stroke-width="1.3"><circle cx="8" cy="8" r="6.5"/><ellipse cx="8" cy="8" rx="3" ry="6.5"/><path d="M1.5 8 H14.5 M2.5 4.5 H13.5 M2.5 11.5 H13.5"/></svg>
          www.lanternfold.com
        </li>
        <li class="contact__item">
          <svg class="contact__icon" viewBox="0 0 16 16" fill="none" stroke="#fff" stroke-width="1.4"><rect x="1" y="3.5" width="14" height="10"/><path d="M1 3.5 L8 9 L15 3.5"/></svg>
          hello@lanternfold.com
        </li>
        <li class="contact__item">
          <svg class="contact__icon" viewBox="0 0 16 16"><path d="M8 1 L15.5 8 L13.5 8 L13.5 15 L9.5 15 L9.5 10.5 L6.5 10.5 L6.5 15 L2.5 15 L2.5 8 L0.5 8 Z" fill="#fff"/></svg>
          Harbor Point, Eastvale
        </li>
      </ul>
    </div>
  </section>

</body>
</html>
```